Pop-up Banner

Would like a design for a pop-up 85 x 206cm banner for a trade show. (from norla press)
We would like "our logo" (brightwave holdings) - then the tagline - "Your Trusted Partner in Data-Driven Decisions"
*Supporting Bullets*
Unified data, analytics & AI
Trusted insights, faster outcomes
Real-time intelligence at scale
Enterprise-ready, secure solutions
Clarity from data complexity
trusted by...some company logos
Partners with : partner logo
Our Colours: #FFA300, #3D4176, #FDD16E, #F87C57, #A68118, #1C2F36

```html
<!DOCTYPE html>
<html lang="en">
<head>
<meta charset="utf-8">
<title>Brightwave Holdings – Pop-up Banner</title>
<link rel="stylesheet" href="https://fonts.googleapis.com/css2?family=Montserrat:wght@700;800&family=Lexend:wght@400;500&display=swap">
<style>
  :root {
    --orange: #FFA300;
    --orange-deep: #F89A1C;
    --navy: #3D4176;
    --gold: #FDD16E;
    --ink: #1C2F36;
    --night: #05080f;
    --sky: #2f90d9;
    --royal: #2b3483;
    --white: #ffffff;
    --stage: #d9d9d9;
  }
  * { box-sizing: border-box; margin: 0; padding: 0; }
  html, body { width: 1091px; height: 1200px; overflow: hidden; }
  body { background: var(--stage); font-family: "Lexend", sans-serif; position: relative; }

  .banner {
    position: absolute; left: 309px; top: 20px;
    width: 472px; height: 1160px; overflow: hidden;
    background: var(--night);
  }

  .hero {
    position: absolute; left: 0; top: 0; width: 100%; height: 600px;
    background:
      radial-gradient(ellipse at 55% 72%, rgba(47,144,217,.55) 0%, rgba(20,60,110,.35) 30%, rgba(5,8,15,0) 60%),
      linear-gradient(180deg, #05080f 0%, #0a1a2e 45%, #0d2a45 70%, #05080f 100%);
  }

  .brand {
    position: absolute; top: 52px; left: 0; width: 100%;
    display: flex; align-items: center; justify-content: center; gap: 14px;
  }
  .brand-dot { width: 58px; height: 58px; border-radius: 50%; background: var(--gold); flex: none; }
  .brand-name {
    font-family: "Lexend", sans-serif; font-weight: 500; color: var(--gold);
    font-size: 23px; line-height: 1.1; letter-spacing: 1.5px; text-transform: uppercase;
  }

  .headline {
    position: absolute; top: 142px; left: 0; width: 100%; text-align: center;
    font-family: "Montserrat", sans-serif; font-weight: 800;
    font-size: 44px; line-height: 47px; text-transform: uppercase;
    color: var(--white); letter-spacing: -0.5px;
  }
  .headline .accent { color: var(--sky); display: block; }

  .hero-visual {
    position: absolute; left: 0; top: 335px; width: 100%; height: 265px;
    background: radial-gradient(ellipse at 50% 60%, #3aa8e6 0%, #15507f 35%, rgba(10,30,55,.2) 70%, rgba(5,8,15,0) 100%);
  }

  .divider { position: absolute; left: 0; top: 556px; width: 100%; height: 62px; }

  .features {
    position: absolute; left: 0; top: 613px; width: 100%; height: 530px;
    background:
      radial-gradient(circle at 110% 10%, rgba(255,220,120,.35) 0, rgba(255,220,120,0) 30%),
      linear-gradient(180deg, var(--orange) 0%, var(--orange-deep) 100%);
  }
  .feature-list {
    position: absolute; left: 64px; top: 44px; list-style: none;
    font-size: 22px; line-height: 28px; color: #111; font-weight: 400;
  }
  .feature-list li { position: relative; padding-left: 28px; margin-bottom: 0; }
  .feature-list li + li { margin-top: 0; }
  .feature-list svg { position: absolute; left: 0; top: 7px; width: 15px; height: 15px; }

  .trusted {
    position: absolute; left: 30px; top: 257px; width: 415px; height: 210px;
    background: var(--white); border-radius: 14px 14px 0 0;
  }
  .trusted-title {
    display: flex; align-items: center; gap: 12px;
    margin: 22px 36px 0; color: var(--navy); font-weight: 500; font-size: 15px;
  }
  .trusted-title::before, .trusted-title::after { content: ""; flex: 1; height: 1px; background: var(--navy); }
  .client-grid {
    display: grid; grid-template-columns: repeat(3, 1fr); row-gap: 20px;
    margin: 18px 30px 0; align-items: center;
  }
  .client { display: flex; align-items: center; gap: 6px; font-size: 17px; font-weight: 500; color: #333; justify-content: center; }
  .client-mark { width: 16px; height: 16px; flex: none; }
  .c-teal { color: #0f8f73; } .c-teal .client-mark { background: #0f8f73; border-radius: 50%; }
  .c-red { color: #d0402c; }
  .c-blue { color: #1d6fb5; } .c-blue .client-mark { background: #1d6fb5; border-radius: 50%; }
  .c-navy { color: var(--navy); }
  .c-grey { color: #666; } .c-grey .client-mark { background: #777; }
  .c-green { color: #25a75a; }

  .footer {
    position: absolute; left: 0; bottom: 0; width: 100%; height: 97px;
    background: var(--ink); display: flex; align-items: center; justify-content: center;
    font-family: "Montserrat", sans-serif; font-weight: 700; color: var(--white); font-size: 18px;
  }
</style>
</head>
<body>
  <main class="banner">
    <section class="hero">
      <div class="brand">
        <span class="brand-dot"></span>
        <span class="brand-name">Brightwave<br>Holdings</span>
      </div>
      <h1 class="headline">Your Trusted<br>Partner in<span class="accent">Data-Driven<br>Decisions</span></h1>
      <div class="hero-visual" role="img" aria-label="Photo of a hand touching a glowing tablet with rising bar charts and percentage dials"></div>
    </section>

    <svg class="divider" viewBox="0 0 472 62" preserveAspectRatio="none" aria-hidden="true">
      <polygon points="0,30 472,30 472,62 0,62" fill="#FFA300"/>
      <polygon points="0,30 310,30 338,0 472,0 472,28 335,28 308,57 0,57" fill="#2f90d9"/>
      <polygon points="0,46 220,46 250,20 472,20 472,30 360,30 320,62 0,62" fill="#2b3483"/>
    </svg>

    <section class="features">
      <ul class="feature-list">
        <li><svg viewBox="0 0 16 16"><circle cx="8" cy="8" r="8" fill="#111"/><path d="M4.5 8.3l2.3 2.2 4.6-4.8" stroke="#FFA300" stroke-width="2" fill="none"/></svg>Unified data, analytics &amp; AI</li>
        <li><svg viewBox="0 0 16 16"><circle cx="8" cy="8" r="8" fill="#111"/><path d="M4.5 8.3l2.3 2.2 4.6-4.8" stroke="#FFA300" stroke-width="2" fill="none"/></svg>Trusted insights, faster<br>outcomes</li>
        <li><svg viewBox="0 0 16 16"><circle cx="8" cy="8" r="8" fill="#111"/><path d="M4.5 8.3l2.3 2.2 4.6-4.8" stroke="#FFA300" stroke-width="2" fill="none"/></svg>Real-time intelligence at scale</li>
        <li><svg viewBox="0 0 16 16"><circle cx="8" cy="8" r="8" fill="#111"/><path d="M4.5 8.3l2.3 2.2 4.6-4.8" stroke="#FFA300" stroke-width="2" fill="none"/></svg>Enterprise-ready, secure<br>solutions</li>
        <li><svg viewBox="0 0 16 16"><circle cx="8" cy="8" r="8" fill="#111"/><path d="M4.5 8.3l2.3 2.2 4.6-4.8" stroke="#FFA300" stroke-width="2" fill="none"/></svg>Clarity from data complexity</li>
      </ul>

      <div class="trusted">
        <p class="trusted-title">trusted by:</p>
        <div class="client-grid">
          <span class="client c-teal"><span class="client-mark"></span>Kestrel</span>
          <span class="client c-navy">Marrowby</span>
          <span class="client c-green">fieldnote</span>
          <span class="client c-red">Corvane</span>
          <span class="client c-blue"><span class="client-mark"></span>Halden</span>
          <span class="client c-grey"><span class="client-mark"></span>Tesselite</span>
          <span class="client c-red">Harbour Quay</span>
          <span class="client c-navy">Pellform</span>
          <span class="client c-blue">Driftkit</span>
        </div>
      </div>
    </section>

    <footer class="footer">www.brightwave-holdings.com</footer>
  </main>
</body>
</html>
```